International Trading Company, 'VOLA' needs a Business Card

The company name is "VOLA" and it has own logo design.
I'd like to use its logo on this business card.
I need two side Business Card.
I'll look forward to your great design.
Thank you very much in advance.

Contact Information for Business Card

Company Name : Vola Harbor Limited
Information Example
Tobias Wrenfold
Mobile(use icon please) : 1 (555) 014-2290
Tel(use icon please) : 1 (555) 014-6835
Email(use icon please) : tobias27@volaharbor.example
Address(use icon please) : 482 Larkmoor Rd, New York, NY 10199, USA

```html
<!DOCTYPE html>
<html lang="en">
<head>
<meta charset="utf-8">
<title>Vola Harbor Limited — Business Card</title>
<link rel="stylesheet" href="https://fonts.googleapis.com/css2?family=Montserrat:wght@400;600;700;800&display=swap">
<style>
  :root {
    --canvas: #2b2b2b;
    --card-black: #0b0b0b;
    --card-white: #ffffff;
    --logo-grey: #5b5b5b;
    --ink: #111111;
    --muted: #8a8a8a;
    --rule: #b9b9b9;
    --band: #0b0b0b;
    --on-dark: #ffffff;
  }
  * { box-sizing: border-box; margin: 0; padding: 0; }
  html, body { width: 1200px; height: 864px; overflow: hidden; }
  body {
    background: var(--canvas);
    font-family: "Montserrat", Arial, sans-serif;
    display: flex;
    flex-direction: column;
    align-items: center;
    justify-content: center;
    gap: 40px;
  }
  .card {
    width: 640px;
    height: 366px;
    position: relative;
    overflow: hidden;
    box-shadow: 0 10px 28px rgba(0,0,0,.45);
  }
  .wordmark {
    font-weight: 800;
    color: var(--logo-grey);
    letter-spacing: 4px;
    line-height: 1;
  }

  /* Back side */
  .card-back { background: var(--card-black); }
  .card-back .wordmark {
    position: absolute;
    left: 0; right: 0; top: 118px;
    text-align: center;
    font-size: 86px;
  }
  .card-back .web {
    position: absolute;
    left: 0; right: 0; bottom: 40px;
    text-align: center;
    color: var(--on-dark);
    font-size: 17px;
    letter-spacing: .3px;
  }

  /* Front side */
  .card-front { background: var(--card-white); }
  .card-front .wordmark {
    position: absolute;
    left: 58px; top: 124px;
    font-size: 80px;
  }
  .divider {
    position: absolute;
    left: 350px; top: 56px;
    width: 1px; height: 196px;
    background: var(--ink);
  }
  .contact {
    position: absolute;
    left: 374px; top: 54px;
    color: var(--muted);
    font-size: 13px;
    line-height: 1.35;
  }
  .contact .name { color: var(--ink); font-size: 19px; font-weight: 700; line-height: 1.1; }
  .contact .role { margin-bottom: 16px; }
  .contact .address { margin-bottom: 14px; }
  .contact .line { display: flex; align-items: center; gap: 8px; color: #555; }
  .contact .line svg { width: 12px; height: 12px; fill: var(--ink); flex: none; }
  .rule {
    position: absolute;
    left: 0; right: 0; bottom: 58px;
    height: 3px; background: var(--rule);
  }
  .band {
    position: absolute;
    left: 0; right: 0; bottom: 0;
    height: 52px; background: var(--band);
    display: flex; align-items: center; justify-content: center;
  }
  .band .web { color: var(--on-dark); font-size: 16px; letter-spacing: .3px; }
</style>
</head>
<body>
  <section class="card card-back">
    <div class="wordmark">VOLA</div>
    <div class="web">www.volaharbor.example</div>
  </section>

  <section class="card card-front">
    <div class="wordmark">VOLA</div>
    <div class="divider"></div>
    <div class="contact">
      <div class="name">Tobias Wrenfold</div>
      <div class="role">President</div>
      <div class="address">482 Larkmoor Rd, New York,<br>NY 10199, USA</div>
      <div class="line">
        <svg viewBox="0 0 24 24" aria-hidden="true"><path d="M6.6 10.8a15.2 15.2 0 0 0 6.6 6.6l2.2-2.2a1 1 0 0 1 1-.25 11.4 11.4 0 0 0 3.6.57 1 1 0 0 1 1 1V20a1 1 0 0 1-1 1A17 17 0 0 1 3 4a1 1 0 0 1 1-1h3.5a1 1 0 0 1 1 1c0 1.25.2 2.45.57 3.57a1 1 0 0 1-.25 1z"/></svg>
        <span>1 (555) 014-2290</span>
      </div>
      <div class="line">
        <svg viewBox="0 0 24 24" aria-hidden="true"><path d="M7 1h10a2 2 0 0 1 2 2v18a2 2 0 0 1-2 2H7a2 2 0 0 1-2-2V3a2 2 0 0 1 2-2zm0 3v14h10V4zm5 15.5a1 1 0 1 0 0 2 1 1 0 0 0 0-2z"/></svg>
        <span>1 (555) 014-6835</span>
      </div>
      <div class="line">
        <svg viewBox="0 0 24 24" aria-hidden="true"><path d="M2 5h20v14H2zm2 2v.5l8 5 8-5V7zm0 2.9V17h16V9.9l-8 5z"/></svg>
        <span>tobias27@volaharbor.example</span>
      </div>
    </div>
    <div class="rule"></div>
    <div class="band"><span class="web">www.volaharbor.example</span></div>
  </section>
</body>
</html>
```